One of Australia's fastest growing energy maintenance contractors needs a new website

www.panelbrite.com.au
Our business has evolved over the past years and now our website is no longer relevant.
We clean solar panels and we vacuum roof gutters.
We clean solar panels on the roofs of residential houses right up to billion dollar solar farms with in excess of 1 million panels. We offer thermal image testing and bird proofing for our residential and commercial clients and thermal drone imaging services for our solar farm clients.
We vacuum clean roof gutters (using a LoftSuk) on the residential house next door right up to enormous private and public schools, colleges, shopping centres, strat complexes and commercial buildings.
When first built our business had more of a domestic residential skew and the website reflected that. While that is still part of our core business we are now bidding on and have secured large government, commercial and infrastructure contracts and our new website needs to reflect our growth and our new business. We need a new site that it optimised for both desktop ad phone viewing as our latest figures showed that 73% of people visiting our site are on mobile phones. We have an extensive amount of data on Trekmetrics available as well as Bidlinks. Both that would also need integrating with the site along with a few other plugins such as Kembo Chat IQ, Friendwall etc along with SEO key words etc. We are also the winner and finalists over multiple years of the small business of the year awards and we like to proudly and prominently display those on our site.
We are looking for a new site with a modern professional feel / theme
There is a definitive break in our business between the solar Panel cleaning clients and the gutter cleaning clients so we would like a home page that begins with a simple choice:
Solar Panel Cleaning – Gutter Cleaning
With a professional full screen background image (we have hundreds to choose from) and along the bottom a small area with rights reserved etc, phone number etc (at some point in the future we will split these into two businesses but for now it’s what we have).
After that selection is made we would like a repeat of that same scenario but the selection is:
If it’s Solar Panel Cleaning
(new background image)
Government – Infrastructure – Commercial – Residential
If it’s Gutter Cleaning
(new background image)
Government – Strata – Commercial – Residential
After making those choices then onto the relevant pages with background images relevant to each sector and a them that suits (on the residential we would like to keep the link to our trekmetrics reviews) - We will provide copy / text for each relevant page.
Other than that, a menu inclusive of the above and:
Resellers Portal – we will provide a link to this from Kembo CRM)
Customer portal (we will supply a link to this from our booking system)
We also need a page for our Solar Resellers / Partners page but we will give them a link to this, it won’t be listed on the site.
Request a quote page (Again we will provide information from Kembo as this will be linked to the CRM)
Standard contact us page inclusive of phone numbers, address and fields supplied from CRM
Sydney – 02 7391 5084
Southern Highlands – 02 4863 1507
Goulburn – 02 4863 1507
Canberra – 02 6178 3045
Wollongong – 02 4239 7615
sales@panelbrite.com.au
Head Office - Ferndell NSW 2583
ABN: 48762093115
Responsive Design: Optimized for desktop and mobile (73% mobile visitors).
Fast Loading Speed: Optimized for performance.
Smooth Transition Animations: For service and category selection.
Sticky Contact Bar: Always accessible at the bottom of mobile screens for quick calls.
SEO Optimization: Focused on government tenders, large-scale commercial contracts, and infrastructure projects.
Integrations
Trekmetrics & Trekmetrics Bidlinks.
Kembo Chat IQ.
Friendwall Beacon.
SEO tools and keyword optimization.
Many many more images available if needed

```html
<!DOCTYPE html>
<html lang="en">
<head>
<meta charset="utf-8">
<title>Panel Brite – Homepage Screens</title>
<link href="https://fonts.googleapis.com/css2?family=Montserrat:wght@400;500;600;700&display=swap" rel="stylesheet">
<style>
  :root {
    --brand-blue: #0a56b0;
    --band-blue: rgba(22, 96, 190, 0.82);
    --band-blue-soft: rgba(20, 80, 170, 0.72);
    --white: #ffffff;
    --divider: rgba(255, 255, 255, 0.22);
  }
  * { box-sizing: border-box; margin: 0; padding: 0; }
  html, body { width: 1200px; height: 2801px; overflow: hidden; background: var(--white); }
  body { position: relative; font-family: "Montserrat", sans-serif; color: var(--white); }

  .screen { position: absolute; left: 75px; width: 1050px; height: 852px; box-shadow: 0 2px 6px rgba(0,0,0,0.18); overflow: hidden; }
  .screen--choice { top: 71px; }
  .screen--solar { top: 963px; }
  .screen--gutter { top: 1862px; }

  .hero { position: absolute; left: 0; top: 0; width: 1050px; height: 580px; overflow: hidden; }
  .hero-photo { position: absolute; inset: 0; }
  .hero-photo--solar {
    background:
      radial-gradient(ellipse 300px 380px at 60px 330px, rgba(120,140,70,0.85), transparent 70%),
      radial-gradient(ellipse 260px 200px at 900px 120px, rgba(240,240,230,0.6), transparent 70%),
      linear-gradient(160deg, #6e9ac8 0%, #9fbfdc 35%, #3c5f93 60%, #1d3563 80%, #6e6e72 100%);
  }
  .hero-photo--gutter {
    background:
      radial-gradient(ellipse 260px 200px at 220px 460px, rgba(205,130,50,0.75), transparent 70%),
      radial-gradient(ellipse 320px 260px at 850px 120px, rgba(30,110,120,0.8), transparent 70%),
      linear-gradient(170deg, #55606a 0%, #3c4650 40%, #6b5a45 70%, #3a3228 100%);
  }
  .hero-shade { position: absolute; inset: 0; background: rgba(10, 25, 50, 0.18); }

  .split-art { position: absolute; inset: 0; }

  .choice-label {
    position: absolute; height: 54px; display: flex; align-items: center;
    font-weight: 700; font-size: 28px; color: var(--white);
  }
  .choice-label::before {
    content: ""; position: absolute; inset: 0; background: var(--band-blue);
    transform: skewX(-20deg); z-index: 0;
  }
  .choice-label span { position: relative; z-index: 1; }
  .choice-label--solar { left: 83px; top: 262px; width: 386px; padding-left: 41px; }
  .choice-label--gutter { left: 593px; top: 321px; width: 359px; padding-left: 41px; }

  .brand-badge {
    position: absolute; left: 443px; top: 235px; width: 164px; height: 164px; border-radius: 50%;
    background: var(--white); border: 4px solid var(--brand-blue);
    display: flex; align-items: center; justify-content: center;
    font-weight: 600; font-size: 21px; color: var(--brand-blue); z-index: 2;
  }

  .hero-title { position: absolute; left: 0; width: 1050px; text-align: center; }
  .brand-name { top: 150px; font-weight: 600; font-size: 76px; line-height: 90px; text-shadow: 0 2px 6px rgba(0,0,0,0.25); }

  .service-band {
    position: absolute; top: 324px; height: 62px; background: var(--band-blue);
    display: flex; align-items: center; justify-content: center;
    font-weight: 700; font-size: 48px; text-shadow: 0 2px 4px rgba(0,0,0,0.25);
  }
  .sector-band {
    position: absolute; top: 395px; height: 51px; background: var(--band-blue-soft);
    display: flex; align-items: center; justify-content: center;
    font-weight: 500; font-size: 24px;
  }
  .screen--solar .service-band { left: 251px; width: 549px; }
  .screen--solar .sector-band { left: 186px; width: 683px; }
  .screen--gutter .service-band { left: 297px; width: 457px; }
  .screen--gutter .sector-band { left: 211px; width: 627px; }

  .site-footer { position: absolute; left: 0; top: 580px; width: 1050px; height: 272px; background: var(--brand-blue); }
  .footer-brand { position: absolute; left: 130px; top: 80px; font-weight: 700; font-size: 40px; line-height: 48px; color: var(--white); }
  .footer-col { position: absolute; top: 30px; }
  .footer-col--contact { left: 407px; }
  .footer-col--address { left: 688px; }
  .footer-heading { display: flex; align-items: center; gap: 11px; font-weight: 700; font-size: 19px; height: 38px; }
  .icon-ring { width: 38px; height: 38px; border-radius: 50%; border: 1.5px solid var(--white); display: flex; align-items: center; justify-content: center; }
  .footer-list { list-style: none; margin-left: 52px; margin-top: 9px; font-size: 12.5px; line-height: 25.5px; font-weight: 400; }
  .footer-divider { position: absolute; left: 99px; top: 224px; width: 853px; height: 1px; background: var(--divider); }
  .copyright { position: absolute; left: 0; top: 240px; width: 1050px; text-align: center; font-size: 12px; }
</style>
</head>
<body>

<section class="screen screen--choice">
  <div class="hero">
    <svg class="split-art" width="1050" height="580" viewBox="0 0 1050 580" role="img" aria-label="Split photo: technician in hard hat cleaning rooftop solar panels at sunset on the left; gloved hands clearing autumn leaves from a roof gutter on the right">
      <defs>
        <linearGradient id="solarSide" x1="0" y1="0" x2="0.6" y2="1">
          <stop offset="0" stop-color="#c98a2a"/>
          <stop offset="0.35" stop-color="#7c6a4a"/>
          <stop offset="0.65" stop-color="#2c4a78"/>
          <stop offset="1" stop-color="#1a2f55"/>
        </linearGradient>
        <linearGradient id="gutterSide" x1="0" y1="0" x2="1" y2="1">
          <stop offset="0" stop-color="#e3c9a2"/>
          <stop offset="0.35" stop-color="#b9793a"/>
          <stop offset="0.6" stop-color="#5c6f86"/>
          <stop offset="1" stop-color="#6a4a2a"/>
        </linearGradient>
      </defs>
      <polygon points="0,0 604,0 442,580 0,580" fill="url(#solarSide)"/>
      <polygon points="604,0 1050,0 1050,580 442,580" fill="url(#gutterSide)"/>
      <line x1="604" y1="0" x2="442" y2="580" stroke="#ffffff" stroke-width="5"/>
    </svg>
    <div class="choice-label choice-label--solar"><span>Solar Panel Cleaning</span></div>
    <div class="choice-label choice-label--gutter"><span>Gutter Cleaning</span></div>
    <div class="brand-badge">Panel Brite</div>
  </div>
  <footer class="site-footer">
    <div class="footer-brand">Panel Brite</div>
    <div class="footer-col footer-col--contact">
      <div class="footer-heading">
        <span class="icon-ring"><svg width="14" height="14" viewBox="0 0 24 24"><path d="M6.6 10.8a15.1 15.1 0 0 0 6.6 6.6l2.2-2.2a1 1 0 0 1 1-.25 11.4 11.4 0 0 0 3.6.57 1 1 0 0 1 1 1V20a1 1 0 0 1-1 1A17 17 0 0 1 3 4a1 1 0 0 1 1-1h3.5a1 1 0 0 1 1 1c0 1.25.2 2.45.57 3.57a1 1 0 0 1-.25 1z" fill="#fff"/></svg></span>
        CONTACT US
      </div>
      <ul class="footer-list">
        <li>Sydney – 02 7391 5084</li>
        <li>Southern Highlands – 02 4863 1507</li>
        <li>Goulburn – 02 4863 1507</li>
        <li>Canberra – 02 6178 3045</li>
        <li>Wollongong – 02 4239 7615</li>
      </ul>
    </div>
    <div class="footer-col footer-col--address">
      <div class="footer-heading">
        <span class="icon-ring"><svg width="12" height="15" viewBox="0 0 24 30"><path d="M12 0a10 10 0 0 0-10 10c0 7.5 10 20 10 20s10-12.5 10-20A10 10 0 0 0 12 0zm0 14a4 4 0 1 1 0-8 4 4 0 0 1 0 8z" fill="#fff"/></svg></span>
        ADDRESS
      </div>
      <ul class="footer-list">
        <li>sales@panelbrite.com.au</li>
        <li>Head Office - Ferndell NSW 2583</li>
        <li>ABN: 48762093115</li>
      </ul>
    </div>
    <div class="footer-divider"></div>
    <p class="copyright">©2025 Panel Brite. All rights reserved.</p>
  </footer>
</section>

<section class="screen screen--solar">
  <div class="hero">
    <div class="hero-photo hero-photo--solar" role="img" aria-label="Photo of residential rooftop solar panels under a bright sky with blurred garden foliage in the foreground"></div>
    <div class="hero-shade"></div>
    <div class="hero-title brand-name">Panel Brite</div>
    <div class="service-band">Solar Panel Cleaning</div>
    <div class="sector-band">Government – Infrastructure – Commercial – Residential</div>
  </div>
  <footer class="site-footer">
    <div class="footer-brand">Panel Brite</div>
    <div class="footer-col footer-col--contact">
      <div class="footer-heading">
        <span class="icon-ring"><svg width="14" height="14" viewBox="0 0 24 24"><path d="M6.6 10.8a15.1 15.1 0 0 0 6.6 6.6l2.2-2.2a1 1 0 0 1 1-.25 11.4 11.4 0 0 0 3.6.57 1 1 0 0 1 1 1V20a1 1 0 0 1-1 1A17 17 0 0 1 3 4a1 1 0 0 1 1-1h3.5a1 1 0 0 1 1 1c0 1.25.2 2.45.57 3.57a1 1 0 0 1-.25 1z" fill="#fff"/></svg></span>
        CONTACT US
      </div>
      <ul class="footer-list">
        <li>Sydney – 02 7391 5084</li>
        <li>Southern Highlands – 02 4863 1507</li>
        <li>Goulburn – 02 4863 1507</li>
        <li>Canberra – 02 6178 3045</li>
        <li>Wollongong – 02 4239 7615</li>
      </ul>
    </div>
    <div class="footer-col footer-col--address">
      <div class="footer-heading">
        <span class="icon-ring"><svg width="12" height="15" viewBox="0 0 24 30"><path d="M12 0a10 10 0 0 0-10 10c0 7.5 10 20 10 20s10-12.5 10-20A10 10 0 0 0 12 0zm0 14a4 4 0 1 1 0-8 4 4 0 0 1 0 8z" fill="#fff"/></svg></span>
        ADDRESS
      </div>
      <ul class="footer-list">
        <li>sales@panelbrite.com.au</li>
        <li>Head Office - Ferndell NSW 2583</li>
        <li>ABN: 48762093115</li>
      </ul>
    </div>
    <div class="footer-divider"></div>
    <p class="copyright">©2025 Panel Brite. All rights reserved.</p>
  </footer>
</section>

<section class="screen screen--gutter">
  <div class="hero">
    <div class="hero-photo hero-photo--gutter" role="img" aria-label="Photo of a gloved worker clearing autumn leaves from a roof gutter beside dark shingles"></div>
    <div class="hero-shade"></div>
    <div class="hero-title brand-name">Panel Brite</div>
    <div class="service-band">Gutter Cleaning</div>
    <div class="sector-band">Government – Strata – Commercial – Residential</div>
  </div>
  <footer class="site-footer">
    <div class="footer-brand">Panel Brite</div>
    <div class="footer-col footer-col--contact">
      <div class="footer-heading">
        <span class="icon-ring"><svg width="14" height="14" viewBox="0 0 24 24"><path d="M6.6 10.8a15.1 15.1 0 0 0 6.6 6.6l2.2-2.2a1 1 0 0 1 1-.25 11.4 11.4 0 0 0 3.6.57 1 1 0 0 1 1 1V20a1 1 0 0 1-1 1A17 17 0 0 1 3 4a1 1 0 0 1 1-1h3.5a1 1 0 0 1 1 1c0 1.25.2 2.45.57 3.57a1 1 0 0 1-.25 1z" fill="#fff"/></svg></span>
        CONTACT US
      </div>
      <ul class="footer-list">
        <li>Sydney – 02 7391 5084</li>
        <li>Southern Highlands – 02 4863 1507</li>
        <li>Goulburn – 02 4863 1507</li>
        <li>Canberra – 02 6178 3045</li>
        <li>Wollongong – 02 4239 7615</li>
      </ul>
    </div>
    <div class="footer-col footer-col--address">
      <div class="footer-heading">
        <span class="icon-ring"><svg width="12" height="15" viewBox="0 0 24 30"><path d="M12 0a10 10 0 0 0-10 10c0 7.5 10 20 10 20s10-12.5 10-20A10 10 0 0 0 12 0zm0 14a4 4 0 1 1 0-8 4 4 0 0 1 0 8z" fill="#fff"/></svg></span>
        ADDRESS
      </div>
      <ul class="footer-list">
        <li>sales@panelbrite.com.au</li>
        <li>Head Office - Ferndell NSW 2583</li>
        <li>ABN: 48762093115</li>
      </ul>
    </div>
    <div class="footer-divider"></div>
    <p class="copyright">©2025 Panel Brite. All rights reserved.</p>
  </footer>
</section>

</body>
</html>
```